Stationery Design Project

QV7 Staffing requires letterhead and business card designs for a company based in London. Just like the name, we're a management resourcing company, providing resources to third party companies. You can see www.qv7staffing-example.com for ideas on existing colour schemes and design concepts that have been implimented and agreed to. Ultimately the design should broadcast professionalism, safety and the concept of growth.

Target Market(s)

Financial institutes; friendly societies (All UK based)

Industry/Entity Type

Safety

Requirements
Must have
• Files produced should be print ready; and the text in them editable (eg address, name etc)

```html
<!DOCTYPE html>
<html lang="en">
<head>
<meta charset="utf-8">
<title>QV7 Staffing — Stationery</title>
<link rel="stylesheet" href="https://fonts.googleapis.com/css2?family=Arimo:wght@400;700&display=swap">
<style>
  :root {
    --stage: #8f8f8f;
    --label: #ffffff;
    --teal: #2497ad;
    --teal-dark: #1b8398;
    --sky: #8cd0ea;
    --sky-soft: #cfe9f3;
    --mist: #c9dbe2;
    --circle-grey: #c4c4c4;
    --card-light: #f7f7f7;
    --card-edge: #dcdcdc;
    --paper: #ffffff;
  }
  * { box-sizing: border-box; margin: 0; padding: 0; }
  html, body { width: 1200px; height: 900px; overflow: hidden; }
  body {
    background: var(--stage);
    font-family: "Arimo", Arial, sans-serif;
    position: relative;
  }
  .section-label {
    position: absolute;
    color: var(--label);
    font-weight: 700;
    font-size: 40px;
    letter-spacing: 1px;
    text-align: center;
  }
  .label-back { left: 124px; width: 312px; top: 63px; }
  .label-front { left: 124px; width: 312px; top: 824px; }
  .label-letterhead { left: 530px; width: 585px; top: 63px; }

  .frame { position: absolute; border: 2px solid var(--label); }
  .frame-back { left: 124px; top: 110px; width: 312px; height: 225px; }
  .frame-front { left: 124px; top: 598px; width: 312px; height: 225px; }
  .frame-letterhead { left: 530px; top: 112px; width: 585px; height: 710px; }

  .business-card {
    position: absolute;
    width: 244px; height: 140px;
    background: radial-gradient(circle at 45% 40%, #ffffff 0%, var(--card-light) 45%, var(--card-edge) 100%);
    overflow: hidden;
  }
  .card-back { left: 158px; top: 152px; }
  .card-front { left: 158px; top: 640px; }
  .business-card svg.card-art { position: absolute; inset: 0; }

  .brand-name {
    position: absolute;
    color: var(--teal);
    font-weight: 700;
    white-space: nowrap;
  }
  .card-back .brand-name { right: 10px; top: 10px; font-size: 11px; }
  .card-front .brand-name { left: 10px; top: 52px; font-size: 21px; }

  .contact-list {
    position: absolute; left: 7px; top: 7px;
    list-style: none;
    color: var(--teal);
    font-size: 7.6px;
    line-height: 13.8px;
  }

  .letterhead {
    position: absolute;
    left: 594px; top: 165px;
    width: 459px; height: 594px;
    background: var(--paper);
  }
  .letterhead svg.sheet-art { position: absolute; inset: 0; }
  .letterhead .brand-name { left: 14px; top: 20px; font-size: 17px; }
  .sender-field {
    position: absolute;
    color: var(--teal);
    font-weight: 700;
    font-size: 7px;
  }
  .sender-name { left: 155px; top: 13px; }
  .sender-address { left: 155px; top: 33px; }
</style>
</head>
<body>
  <div class="section-label label-back">Back</div>
  <div class="section-label label-letterhead">Letter Head</div>
  <div class="section-label label-front">Front</div>

  <div class="frame frame-back"></div>
  <div class="frame frame-front"></div>
  <div class="frame frame-letterhead"></div>

  <!-- Business card: reverse side -->
  <div class="business-card card-back">
    <svg class="card-art" width="244" height="140" viewBox="0 0 244 140">
      <circle cx="114" cy="16" r="9" fill="var(--sky)" opacity="0.8"/>
      <circle cx="156" cy="43" r="26" fill="var(--circle-grey)"/>
      <path d="M0 126 Q110 96 244 118 L244 140 L0 140 Z" fill="var(--mist)"/>
      <path d="M0 132 Q120 108 244 126 L244 140 L0 140 Z" fill="var(--sky-soft)"/>
      <path d="M208 140 A40 40 0 0 1 244 104" fill="none" stroke="var(--sky)" stroke-width="5"/>
      <path d="M224 140 A26 26 0 0 1 244 116" fill="none" stroke="var(--sky-soft)" stroke-width="4"/>
    </svg>
    <div class="brand-name">QV7 Staffing</div>
    <ul class="contact-list">
      <li>Name Here</li>
      <li>Job Title Here</li>
      <li>Email Address Here</li>
      <li>Mobile Num Here</li>
      <li>Landline Num Here</li>
      <li>Business Address Here</li>
    </ul>
  </div>

  <!-- Business card: front side -->
  <div class="business-card card-front">
    <svg class="card-art" width="244" height="140" viewBox="0 0 244 140">
      <path d="M200 0 A30 30 0 0 0 230 30" fill="none" stroke="var(--sky-soft)" stroke-width="5"/>
      <path d="M214 0 A30 30 0 0 0 244 30" fill="none" stroke="var(--sky-soft)" stroke-width="5"/>
      <circle cx="195" cy="26" r="20" fill="var(--mist)"/>
      <circle cx="215" cy="67" r="8" fill="var(--sky)"/>
      <path d="M0 128 Q110 100 244 118 L244 140 L0 140 Z" fill="var(--mist)"/>
      <path d="M0 134 Q120 112 244 126 L244 140 L0 140 Z" fill="var(--sky-soft)"/>
    </svg>
    <div class="brand-name">QV7 Staffing</div>
  </div>

  <!-- Letterhead -->
  <div class="letterhead">
    <svg class="sheet-art" width="459" height="594" viewBox="0 0 459 594">
      <path d="M0 10 A40 40 0 0 0 38 0" fill="none" stroke="var(--sky-soft)" stroke-width="5"/>
      <circle cx="136" cy="0" r="17" fill="var(--sky-soft)" opacity="0.8"/>
      <circle cx="78" cy="42" r="7" fill="var(--sky-soft)"/>
      <line x1="155" y1="24" x2="371" y2="24" stroke="var(--sky)" stroke-width="2"/>
      <line x1="99" y1="44" x2="371" y2="44" stroke="var(--teal-dark)" stroke-width="2"/>
      <line x1="19" y1="68" x2="19" y2="340" stroke="var(--teal)" stroke-width="2"/>
      <line x1="36" y1="68" x2="36" y2="284" stroke="var(--sky)" stroke-width="2"/>
    </svg>
    <div class="brand-name">QV7 Staffing</div>
    <div class="sender-field sender-name">Name Here</div>
    <div class="sender-field sender-address">Address Here</div>
  </div>
</body>
</html>
```